I already have a logo created by Sketch Harbor that I'm very happy with. I need to spruce up my business card now. Its a double sided card with not much info on it, I like to keep it simple.
Front of card: name, phone # email address, web address. Tag Line "Outsourced Technology Solutions", under that it says Business Voice Services & Electronic Protection.
Rear of Card: Content written inside a "cloud" saying "Cloud Solutions" "Cloud Integrity"

Target Market(s)

Business to Business

Industry/Entity Type

Business

Contact Information for Business Card

We are in the technology field. Providing Telephone systems (hardware), SIP Trunks (dial tone/local/long distance/telephone #'s), LAN (Local Area Network)infrastructure cabling, Data Center solutions and Security Applications (Camera systems, Access Control systems,

Requirements
Must have
• Must have brevity
Should not have
• Clutter and/or too much information

```html
<!DOCTYPE html>
<html lang="en">
<head>
<meta charset="utf-8">
<title>Summit Linked Communications – Business Card</title>
<link rel="stylesheet" href="https://fonts.googleapis.com/css2?family=Source+Sans+3:wght@400;600;700&display=swap">
<style>
  :root {
    --backdrop: #2b2b2d;
    --card: #f4f4f5;
    --brand-blue: #1f4a8f;
    --text-grey: #555a60;
    --tagline-grey: #9a9ea4;
    --rule: #c9cbce;
    --deco: #e4e5e7;
  }
  * { box-sizing: border-box; margin: 0; padding: 0; }
  html, body { width: 1200px; height: 900px; overflow: hidden; }
  body {
    background: var(--backdrop);
    font-family: "Source Sans 3", Arial, sans-serif;
    display: flex;
    align-items: center;
    justify-content: center;
    gap: 40px;
  }
  .card {
    position: relative;
    width: 540px;
    height: 310px;
    background: var(--card);
    border-radius: 22px;
    overflow: hidden;
  }

  /* Front */
  .brand { position: absolute; left: 40px; top: 44px; }
  .brand-name {
    display: flex; align-items: center; gap: 10px;
    color: var(--brand-blue); font-weight: 600; font-size: 24px; line-height: 1;
  }
  .brand-mark { width: 14px; height: 14px; background: var(--brand-blue); }
  .brand-tagline {
    margin-top: 6px; color: var(--tagline-grey); font-size: 17px; letter-spacing: .3px;
    padding-bottom: 6px; border-bottom: 1px solid var(--rule); width: 290px;
  }
  .person { position: absolute; right: 40px; top: 112px; text-align: right; }
  .person-name { color: var(--brand-blue); font-weight: 700; font-size: 19px; }
  .person-role {
    color: var(--text-grey); font-size: 14px; border-top: 1px solid var(--rule);
    padding-top: 2px; margin-top: 2px;
  }
  .contact { position: absolute; left: 40px; top: 196px; width: 460px; border-top: 1px solid var(--rule); padding-top: 8px; }
  .contact-line { display: flex; align-items: center; gap: 10px; color: var(--text-grey); font-size: 15px; line-height: 21px; }
  .contact-line svg { width: 11px; height: 11px; fill: var(--brand-blue); }
  .services-line { position: absolute; right: 40px; bottom: 22px; color: var(--text-grey); font-size: 15px; }

  /* Back */
  .service-list { position: absolute; left: 40px; top: 40px; }
  .service-group + .service-group { margin-top: 6px; }
  .service-heading { color: var(--brand-blue); font-weight: 700; font-size: 15px; line-height: 18px; }
  .service-item { color: var(--text-grey); font-size: 15px; line-height: 18px; padding-left: 12px; }
  .back-decoration { position: absolute; right: -60px; top: -40px; }
</style>
</head>
<body>

  <section class="card card-front">
    <div class="brand">
      <div class="brand-name"><span class="brand-mark"></span>Summit Linked Communications, LLC</div>
      <div class="brand-tagline">Outsourced Technology Solutions</div>
    </div>
    <div class="person">
      <div class="person-name">Marcus Hale</div>
      <div class="person-role">Managing Director</div>
    </div>
    <div class="contact">
      <div class="contact-line">
        <svg viewBox="0 0 12 12"><path d="M2.5 0.5 L4.5 0.5 L5.2 3 L3.9 4.2 Q5 6.8 7.8 8.1 L9 6.8 L11.5 7.5 L11.5 9.5 Q11.5 11.5 9.5 11.5 Q1 11 0.5 2.5 Q0.5 0.5 2.5 0.5 Z"/></svg>
        044-555 010 234
      </div>
      <div class="contact-line">
        <svg viewBox="0 0 12 12"><path d="M0 2 H12 V10 H0 Z M0.8 2.6 L6 6.6 L11.2 2.6"/></svg>
        info@summitlinked.com
      </div>
      <div class="contact-line">
        <svg viewBox="0 0 12 12"><circle cx="6" cy="6" r="6"/></svg>
        www.summitlinked.com
      </div>
    </div>
    <div class="services-line">Voice Services, Networking &amp; Electronic Protection</div>
  </section>

  <section class="card card-back">
    <div class="service-list">
      <div class="service-group">
        <div class="service-heading">Voice Services:</div>
        <div class="service-item">Premise PBX</div>
        <div class="service-item">SIP Trunking</div>
        <div class="service-item">Hosted PBX</div>
      </div>
      <div class="service-group">
        <div class="service-heading">Network Services:</div>
        <div class="service-item">Infrastructure</div>
        <div class="service-item">Network Services</div>
        <div class="service-item">Data Center Solutions</div>
        <div class="service-item">Network Security</div>
      </div>
      <div class="service-group">
        <div class="service-heading">Electronic Protection:</div>
        <div class="service-item">CCTV</div>
        <div class="service-item">Access Control</div>
        <div class="service-item">Central Station Monitoring</div>
      </div>
    </div>
    <svg class="back-decoration" width="280" height="280" viewBox="0 0 280 280" aria-hidden="true">
      <circle cx="140" cy="140" r="130" fill="var(--deco)"/>
    </svg>
  </section>

</body>
</html>
```